Business Card Design for Lawn Management

Lawn Management

Industry/Entity Type

Business

Contact Information for Business Card

Calloway Lawn Management
Doran Calloway
Calloway_Lawn@brindlemail.com
404-627-1845

```html
<!DOCTYPE html>
<html lang="en">
<head>
<meta charset="utf-8">
<title>Calloway Lawn Management – Business Card</title>
<link rel="stylesheet" href="https://fonts.googleapis.com/css2?family=Oswald:wght@600&family=Tinos&family=Arimo&display=swap">
<style>
  :root {
    --paper: #ffffff;
    --panel-tint: #f6f6f6;
    --frame: #1a1a1a;
    --leaf-green: #3a8e2a;
    --lime: #8cc63f;
    --lime-light: #a6d24a;
    --fade: #f3f9ea;
    --ghost: #e6e7e8;
    --ink-white: #ffffff;
  }
  html, body {
    margin: 0;
    padding: 0;
    width: 1017px;
    height: 1200px;
    overflow: hidden;
    background: var(--paper);
  }
  .sheet { display: block; width: 1017px; height: 1200px; }
  .card-frame { fill: none; stroke: var(--frame); stroke-width: 1.5; }
  .brand-name { font-family: "Oswald", "Arial Narrow", sans-serif; font-weight: 600; fill: var(--leaf-green); }
  .brand-tagline { font-family: "Arimo", Arial, sans-serif; fill: var(--leaf-green); }
  .serif-white { font-family: "Tinos", "Times New Roman", serif; fill: var(--ink-white); }
  .sans-white { font-family: "Arimo", Arial, sans-serif; fill: var(--ink-white); }
</style>
</head>
<body>
<svg class="sheet" viewBox="0 0 1017 1200" xmlns="http://www.w3.org/2000/svg" aria-label="Calloway Lawn Management business card, front and back">
  <defs>
    <linearGradient id="back-wash" x1="0" y1="0" x2="0" y2="1">
      <stop offset="0" stop-color="#9ccb3b"/>
      <stop offset="0.5" stop-color="#c7e293"/>
      <stop offset="0.85" stop-color="var(--fade)"/>
      <stop offset="1" stop-color="#ffffff"/>
    </linearGradient>
    <linearGradient id="swoosh" x1="0" y1="0" x2="0" y2="1">
      <stop offset="0" stop-color="var(--lime)"/>
      <stop offset="1" stop-color="#5aa832"/>
    </linearGradient>
  </defs>

  <!-- Front side -->
  <g class="card-front">
    <rect class="card-frame" x="2" y="2" width="1012" height="578"/>
    <rect x="19" y="19" width="978" height="543" fill="var(--paper)"/>
    <path class="front-panel" d="M19 19 H386 C280 40 200 90 214 174 C228 300 320 420 371 530 L371 562 H19 Z" fill="var(--panel-tint)"/>
    <path class="front-swoosh" d="M386 19 C280 40 200 90 214 174 C228 300 320 420 371 530 C335 430 238 300 225 180 C215 95 290 40 386 19 Z" fill="url(#swoosh)"/>
    <circle class="ghost-disc" cx="180" cy="420" r="90" fill="var(--ghost)"/>
    <rect class="card-frame" x="19" y="19" width="978" height="543"/>

    <g class="brand-lockup">
      <rect x="623" y="220" width="44" height="44" fill="var(--leaf-green)"/>
      <text class="brand-name" x="647" y="370" font-size="62" text-anchor="middle" letter-spacing="1">CALLOWAY</text>
      <text class="brand-tagline" x="781" y="392" font-size="18" text-anchor="end">Lawn Management</text>
    </g>
  </g>

  <!-- Back side -->
  <g class="card-back">
    <rect class="card-frame" x="2" y="619" width="1012" height="578"/>
    <rect x="19" y="636" width="978" height="542" fill="url(#back-wash)"/>

    <text class="serif-white owner-name" font-size="44" text-anchor="end">
      <tspan x="951" y="713">Doran Calloway</tspan>
      <tspan x="949" y="766">Calloway</tspan>
    </text>

    <text class="serif-white company-name" font-size="44" text-anchor="middle">
      <tspan x="262" y="892">Calloway Lawn</tspan>
      <tspan x="262" y="946">Management,</tspan>
    </text>

    <rect class="divider" x="461" y="826" width="4" height="162" fill="var(--ink-white)"/>

    <path class="contact-band" d="M19 1085 H413 L453 1154 H997 V1178 H19 Z" fill="var(--leaf-green)"/>
    <circle class="corner-disc" cx="910" cy="1100" r="60" fill="var(--leaf-green)"/>

    <text class="sans-white contact-email" x="34" y="1124" font-size="25">Calloway_Lawn@brindlemail.com</text>
    <text class="serif-white contact-phone" x="397" y="1159" font-size="28" text-anchor="end">404-627-1845</text>

    <rect class="card-frame" x="19" y="636" width="978" height="542"/>
  </g>
</svg>
</body>
</html>
```